Business card for Drone Aerial

I need a business card designed keeping in mind I want to do post cards also with a similar design.
Both sides of the card would be cool.
I have a skylark 5 max and would like a picture of it on the front of the card. Similar to one I attached.
I really like the look of a drone in the air and the background pic a little blurry. I attached a few images as IDEAS.
Some special things I want to be on the card additional to the normal business card info:
"Aerial Photography" or "Low Altitude Aerial Photography"?
"ZQB# 90817263"

I like modern and creative. My Favorite color is blue and I like blue on white.
I do not have a business name and am not going to have one. When they read "Aerial Photography" and see the drone and image they will know what the card is for.

FYI, The attached pictures are just images from framewillow and just samples/ideas.

Target Market(s)

Real estate, construction, events

Industry/Entity Type

Business

Contact Information for Business Card

Also Definitely want to contain, my name, my number and email address.

Requirements
Must have
• "ZQB# 90817263"
• "Aerial Photography"

```html
<!DOCTYPE html>
<html lang="en">
<head>
<meta charset="utf-8">
<title>Aerial Photography Business Card</title>
<link rel="stylesheet" href="https://fonts.googleapis.com/css2?family=Arimo:wght@400;700&display=swap">
<style>
  :root {
    --page-bg: #e9ebef;
    --brand-blue: #2a5aa6;
    --band-blue: rgba(74, 130, 210, 0.78);
    --ink-dark: #1f1f24;
    --card-white: #ffffff;
    --sky-top: #8f9cc6;
    --sky-mid: #b4b6d6;
    --city-low: #6f7aa6;
    --water: #5d6a93;
    --drone-light: #eceef4;
    --drone-shade: #c4c9da;
  }
  * { margin: 0; padding: 0; box-sizing: border-box; }
  html, body { width: 1200px; height: 871px; overflow: hidden; }
  body {
    background: var(--page-bg);
    font-family: "Arimo", Arial, sans-serif;
    position: relative;
  }
  .card {
    position: absolute;
    width: 560px;
    height: 320px;
    overflow: hidden;
    box-shadow: 0 10px 28px rgba(20, 30, 60, 0.22);
  }
  /* Front side */
  .card-front { left: 70px; top: 110px; }
  .front-photo {
    position: absolute; inset: 0;
    background: linear-gradient(180deg, var(--sky-top) 0%, var(--sky-mid) 38%, #c3b3cf 62%, var(--city-low) 80%, var(--water) 100%);
  }
  .drone-photo {
    position: absolute; left: 372px; top: 28px;
    width: 168px; height: 96px;
    border-radius: 8px;
    background: linear-gradient(180deg, var(--drone-light) 0%, var(--drone-shade) 100%);
    box-shadow: 0 4px 10px rgba(40, 50, 90, 0.25);
    z-index: 2;
  }
  .title-band {
    position: absolute; left: 0; right: 0; top: 118px; height: 84px;
    background: var(--band-blue);
    display: flex; align-items: center;
    padding-left: 46px;
  }
  .tagline {
    color: #f4f7ff;
    font-weight: 700;
    font-size: 22px;
    letter-spacing: 0.2px;
  }
  .licence-line {
    position: absolute; left: 46px; bottom: 22px;
    color: #f4f7ff;
    font-size: 14px;
    font-weight: 700;
    letter-spacing: 0.5px;
  }
  /* Back side */
  .card-back { left: 570px; top: 440px; background: var(--card-white); }
  .accent-shape { position: absolute; inset: 0; }
  .drone-icon {
    position: absolute; left: 70px; top: 80px;
    width: 110px; height: 100px;
    background: linear-gradient(180deg, #e3ebf7, #cddcf0);
    border-radius: 6px;
  }
  .contact-block {
    position: absolute; left: 270px; top: 84px;
    color: var(--ink-dark);
  }
  .person-name {
    color: var(--brand-blue);
    font-weight: 700;
    font-size: 33px;
    margin-bottom: 14px;
  }
  .contact-list { list-style: none; font-size: 15px; }
  .contact-item { display: flex; align-items: center; gap: 12px; height: 24px; }
  .contact-icon { width: 16px; height: 16px; flex: none; }
</style>
</head>
<body>
  <section class="card card-front" aria-label="Card front">
    <div class="front-photo" role="img" aria-label="Blurred city skyline at dusk over water"></div>
    <div class="drone-photo" role="img" aria-label="White quadcopter drone hovering in the air"></div>
    <div class="title-band">
      <p class="tagline">Low Altitude Aerial Photography</p>
    </div>
    <p class="licence-line">ZQB# 90817263</p>
  </section>

  <section class="card card-back" aria-label="Card back">
    <svg class="accent-shape" viewBox="0 0 560 320" preserveAspectRatio="none" aria-hidden="true">
      <polygon points="348,0 560,0 560,52 356,22" fill="var(--brand-blue)"/>
      <polygon points="0,254 248,296 260,320 0,320" fill="var(--brand-blue)"/>
    </svg>
    <div class="drone-icon" role="img" aria-label="Line icon of a drone spraying"></div>
    <div class="contact-block">
      <h1 class="person-name">Rowan Keller</h1>
      <ul class="contact-list">
        <li class="contact-item">
          <svg class="contact-icon" viewBox="0 0 16 16" aria-hidden="true"><path d="M2 6c0-3 12-3 12 0v1h-3V5.5H5V7H2z M4 8h8l1 6H3z" fill="none" stroke="var(--brand-blue)" stroke-width="1.3"/></svg>
          <span>555 013 4471</span>
        </li>
        <li class="contact-item">
          <svg class="contact-icon" viewBox="0 0 16 16" aria-hidden="true"><rect x="4" y="1.5" width="8" height="13" rx="1.5" fill="none" stroke="var(--brand-blue)" stroke-width="1.3"/><line x1="7" y1="12" x2="9" y2="12" stroke="var(--brand-blue)" stroke-width="1.3"/></svg>
          <span>555 013 4472</span>
        </li>
        <li class="contact-item">
          <svg class="contact-icon" viewBox="0 0 16 16" aria-hidden="true"><rect x="1.5" y="3.5" width="13" height="9" fill="none" stroke="var(--brand-blue)" stroke-width="1.3"/><polyline points="1.5,3.5 8,9 14.5,3.5" fill="none" stroke="var(--brand-blue)" stroke-width="1.3"/></svg>
          <span>rowankeller@mailbox.example</span>
        </li>
      </ul>
    </div>
  </section>
</body>
</html>
```